Quillory Nest Business Card

I need a business card design. We are a collaborate online training company. Our colors are gray and green. Our website is QuilloryNest.com

I would like an area for a profile picture within the card

```html
<!DOCTYPE html>
<html lang="en">
<head>
<meta charset="utf-8">
<title>Quillory Nest Business Card</title>
<link href="https://fonts.googleapis.com/css2?family=Arimo:wght@400;700&display=swap" rel="stylesheet">
<style>
  :root {
    --page: #d9d6d0;
    --card: #2c3033;
    --card-dark: #1f2224;
    --band: #25292b;
    --green: #7ac231;
    --ink: #f2f2f2;
    --muted: #c9cccd;
  }
  * { margin: 0; padding: 0; box-sizing: border-box; }
  html, body { width: 1200px; height: 800px; overflow: hidden; }
  body {
    background: var(--page);
    font-family: "Arimo", Arial, sans-serif;
    display: flex; flex-direction: column; align-items: center; justify-content: center;
    gap: 36px;
  }
  .card {
    position: relative;
    width: 630px; height: 360px;
    background: linear-gradient(160deg, #33383b 0%, var(--card) 55%, #272a2c 100%);
    border-radius: 4px;
    box-shadow: 0 10px 24px rgba(0,0,0,.25);
    overflow: hidden;
  }
  .brand { display: flex; align-items: center; gap: 8px; color: var(--green); font-weight: 700; }
  .brand-dot { width: 14px; height: 14px; border-radius: 50%; background: var(--green); }

  /* back */
  .card-back .band {
    position: absolute; left: 0; right: 0; top: 90px; height: 150px;
    background: var(--card-dark);
    border-top: 3px solid var(--green); border-bottom: 3px solid var(--green);
    display: flex; align-items: center; justify-content: center;
  }
  .card-back .brand { font-size: 44px; gap: 16px; }
  .card-back .brand-dot { width: 40px; height: 40px; }
  .card-back .back-site {
    position: absolute; left: 0; right: 0; bottom: 38px;
    text-align: center; color: var(--muted); font-size: 15px; letter-spacing: .5px;
  }

  /* front */
  .card-front .top-band {
    position: absolute; left: 0; right: 0; top: 0; height: 42px;
    background: var(--card-dark);
    border-bottom: 3px solid var(--green);
  }
  .card-front .brand { position: absolute; right: 24px; top: 58px; font-size: 20px; }
  .profile-photo {
    position: absolute; left: 100px; top: 82px;
    width: 150px; height: 150px; border-radius: 50%;
    background: #363b3e;
    border: 3px solid var(--green);
  }
  .identity { position: absolute; left: 52px; top: 250px; width: 250px; text-align: center; }
  .person-name { color: var(--ink); font-size: 28px; font-weight: 700; letter-spacing: 2px; }
  .person-role { color: var(--green); font-size: 13px; letter-spacing: 1px; margin-top: 4px; }
  .divider {
    position: absolute; left: 320px; top: 140px; width: 3px; height: 160px;
    background: var(--green);
  }
  .contacts { position: absolute; left: 345px; top: 148px; list-style: none; }
  .contacts li {
    display: flex; align-items: flex-start; gap: 10px;
    color: var(--ink); font-size: 15px; line-height: 1.35; margin-bottom: 6px; letter-spacing: .4px;
  }
  .contacts svg { width: 15px; height: 15px; flex: none; margin-top: 2px; }
</style>
</head>
<body>

  <section class="card card-back">
    <div class="band">
      <div class="brand"><span class="brand-dot"></span>Quillory Nest</div>
    </div>
    <p class="back-site">www.quillorynest.com</p>
  </section>

  <section class="card card-front">
    <div class="top-band"></div>
    <div class="brand"><span class="brand-dot"></span>Quillory Nest</div>

    <div class="profile-photo" role="img" aria-label="Profile photo area"></div>
    <div class="identity">
      <h1 class="person-name">R MADDOX</h1>
      <p class="person-role">ADMINISTRATIVE OFFICER</p>
    </div>

    <div class="divider"></div>

    <ul class="contacts">
      <li>
        <svg viewBox="0 0 24 24" fill="#7ac231"><path d="M6.6 10.8a15 15 0 0 0 6.6 6.6l2.2-2.2c.3-.3.7-.4 1-.2 1.1.4 2.3.6 3.6.6.6 0 1 .4 1 1V20c0 .6-.4 1-1 1A17 17 0 0 1 3 4c0-.6.4-1 1-1h3.5c.6 0 1 .4 1 1 0 1.3.2 2.5.6 3.6.1.3 0 .7-.2 1z"/></svg>
        (302) 555-0147
      </li>
      <li>
        <svg viewBox="0 0 24 24" fill="#7ac231"><path d="M2 5h20v14H2z M3 6l9 7 9-7" stroke="#2c3033" stroke-width="1.5"/></svg>
        info@quillorynest.com
      </li>
      <li>
        <svg viewBox="0 0 24 24" fill="none" stroke="#7ac231" stroke-width="2"><circle cx="12" cy="12" r="9"/><path d="M3 12h18M12 3c3 3 3 15 0 18M12 3c-3 3-3 15 0 18"/></svg>
        www.quillorynest.com
      </li>
      <li>
        <svg viewBox="0 0 24 24" fill="#7ac231"><path d="M12 2a7 7 0 0 0-7 7c0 5 7 13 7 13s7-8 7-13a7 7 0 0 0-7-7zm0 9.5A2.5 2.5 0 1 1 12 6.5a2.5 2.5 0 0 1 0 5z"/></svg>
        <span>482 Larkmoor Ave. Suite 7<br>Fenwick, Arizona 85390</span>
      </li>
    </ul>
  </section>

</body>
</html>
```